Solar Panel Cleaning Business Needs a Flyer DL Size

Looking for an advertising flyer in DL Size back and front in high resolution.

Flyer to be vertical.

The front needs to pop, however look very clean and professional that attracts someone to read on and book the service.

The back can be pretty simple but also needs to look good.

Please refer to my website www.brightvanepanelwash.com.au

All information on my business can be found there along with logo, pricing, contact and service information.

The biggest thing to highlight is WHY? Why do you need your solar panels cleaned?

Target Market(s)

Residential Home Owners

Industry/Entity Type

Business

Font styles to use
Serif
Sans Serif
Other font styles liked:
• Don't Mind - Up to Designer

Colors

Designer to choose colors to be used in the design.

Requirements
Must have
• Logo - Services - Pricing - Contact

```html
<!DOCTYPE html>
<html lang="en">
<head>
<meta charset="utf-8">
<title>Brightvane Panel Wash – DL Flyer</title>
<link href="https://fonts.googleapis.com/css2?family=Lato:wght@300;400;700;900&family=Roboto:wght@500&display=swap" rel="stylesheet">
<style>
  :root{
    --green:#2bdc1e;
    --blue:#1357c4;
    --dark:#333333;
    --light:#efefef;
    --ink:#2a2a2a;
    --page:#f4f4f4;
  }
  *{box-sizing:border-box;margin:0;padding:0}
  html,body{width:1200px;height:1200px;overflow:hidden;background:var(--page)}
  body{font-family:"Lato",sans-serif;color:var(--ink)}
  .stage{position:absolute;left:0;top:0;width:1400px;height:1400px;transform:scale(0.857143);transform-origin:0 0}
  .flyer{position:absolute;top:130px;width:540px;height:1144px;background:#fff;overflow:hidden;box-shadow:0 2px 6px rgba(0,0,0,.12)}
  .flyer--front{left:124px}
  .flyer--back{left:736px}

  /* wordmark: plain name in the body face, one colour, one weight */
  .brand{position:absolute;left:0;right:0;text-align:center;z-index:3}
  .brand__name{display:inline-flex;align-items:center;gap:10px;font-family:"Lato",sans-serif;font-weight:700;font-size:26px;color:var(--dark);background:rgba(255,255,255,.85);padding:6px 14px;border-radius:3px}
  .brand__mark{width:14px;height:14px;background:var(--blue)}

  /* front */
  .hero-art{position:absolute;left:0;top:0}
  .why{position:absolute;left:0;top:375px;width:540px;height:212px;background:linear-gradient(180deg,#2f2f2f,#4c4c4c)}
  .why__line1{position:absolute;left:0;right:0;top:50px;text-align:center;font-family:"Roboto",sans-serif;font-weight:500;font-size:47px;color:#fff}
  .why__line2{position:absolute;left:0;right:0;top:102px;text-align:center;font-weight:300;font-size:60px;color:var(--green)}
  .rule-green{position:absolute;left:0;width:540px;height:7px;background:var(--green)}
  .rule-blue{position:absolute;left:0;width:540px;height:7px;background:var(--blue)}
  .services{position:absolute;left:0;top:605px;width:540px;height:427px;background:linear-gradient(180deg,#e4e4e4,#f6f6f6 40%,#f2f2f2)}
  .services__tab{position:absolute;left:146px;top:0;width:247px;height:38px;background:var(--blue);border-radius:0 0 26px 26px;color:#fff;font-weight:700;font-size:33px;text-align:center;line-height:34px}
  .services__copy{position:absolute;left:35px;right:30px;top:62px;font-size:14.5px;line-height:18.5px;color:#3a3a3a}
  .services__copy p{margin-bottom:20px}
  .hl{color:var(--green);font-weight:700}
  .thumb{position:absolute;top:223px;width:148px;height:140px;border:2px solid var(--green)}
  .thumb--panels{left:90px;background:linear-gradient(160deg,#7fb9e0 0%,#2d5fae 35%,#1c3f86 70%,#2a4f95 100%)}
  .thumb--water{left:309px;background:linear-gradient(180deg,#bcd8ef 0%,#dfe9f1 35%,#9ea4aa 60%,#6a6e72 100%)}
  .thumb__label{position:absolute;top:377px;width:220px;text-align:center;font-size:19px;color:var(--blue)}
  .cta{position:absolute;left:0;top:1032px;width:540px;height:46px;background:var(--green);color:#fff;text-align:center;font-size:17.5px;line-height:19px;padding-top:4px}
  .cta-bar{position:absolute;left:0;top:1078px;width:540px;height:22px;background:var(--dark)}
  .phone-pill{position:absolute;left:118px;top:1078px;width:304px;height:56px;background:var(--dark);border-radius:0 0 30px 30px;color:#fff;font-weight:700;font-size:38px;text-align:center;line-height:56px}

  /* back */
  .pricing-band{position:absolute;left:0;top:283px;width:540px;height:80px;background:var(--dark)}
  .pricing-band__title{position:absolute;left:0;right:0;top:18px;text-align:center;font-weight:700;font-size:35px;color:#fff}
  .intro{position:absolute;left:0;top:370px;width:540px;height:224px;background:linear-gradient(180deg,#dcdcdc,#f1f1f1 18%,#f1f1f1)}
  .intro__name{position:absolute;left:0;right:0;top:26px;text-align:center;font-weight:700;font-size:40px;color:var(--green)}
  .intro__text{position:absolute;left:0;right:0;top:82px;text-align:center;font-size:30px;line-height:37px;color:#2f2f2f}
  .intro__offer{position:absolute;left:0;right:0;top:152px;text-align:center;font-weight:300;font-size:56px;color:var(--blue)}
  .tier{position:absolute;left:45px;width:433px}
  .tier__head{height:56px;background:var(--green);color:#fff;font-weight:700;font-size:35px;text-align:center;line-height:54px;border-radius:2px}
  .tier__price{position:absolute;left:0;top:66px;width:145px;height:60px;background:var(--light);color:var(--blue);font-weight:700;font-size:46px;line-height:60px;text-align:center}
  .tier__note{position:absolute;left:162px;top:72px;font-size:16.5px;line-height:21px;color:#222}
  .footer-rule{position:absolute;left:0;top:1038px;width:540px;height:8px;background:var(--blue)}
  .footer{position:absolute;left:0;top:1046px;width:540px;height:98px;background:linear-gradient(180deg,#2e2e2e,#444)}
  .footer__phone{position:absolute;left:0;right:0;top:6px;text-align:center;font-weight:700;font-size:40px;color:var(--green)}
  .footer__web{position:absolute;left:0;right:0;top:52px;text-align:center;font-size:25px;letter-spacing:3px;color:#fff}
</style>
</head>
<body>
<div class="stage">

  <section class="flyer flyer--front">
    <svg class="hero-art" width="540" height="385" viewBox="0 0 540 385" role="img" aria-label="Photo of a brush cleaning rooftop solar panels">
      <defs>
        <linearGradient id="frontPhoto" x1="0" y1="0" x2="0.3" y2="1">
          <stop offset="0" stop-color="#c9d6e6"/>
          <stop offset="0.3" stop-color="#4d76bd"/>
          <stop offset="0.65" stop-color="#2c4f9c"/>
          <stop offset="1" stop-color="#8a8680"/>
        </linearGradient>
        <linearGradient id="frontFade" x1="0" y1="0" x2="0" y2="1">
          <stop offset="0" stop-color="#fff" stop-opacity="1"/>
          <stop offset="0.55" stop-color="#fff" stop-opacity="0.4"/>
          <stop offset="1" stop-color="#fff" stop-opacity="0"/>
        </linearGradient>
      </defs>
      <path d="M0,0 H540 V248 C480,330 400,368 250,370 H0 Z" fill="url(#frontPhoto)"/>
      <rect x="0" y="0" width="540" height="140" fill="url(#frontFade)"/>
      <path d="M0,385 V370 H250 C400,368 480,330 540,248 V385 Z" fill="#2f2f2f"/>
      <path d="M0,372 H250 C400,370 480,332 540,250" fill="none" stroke="#2bdc1e" stroke-width="7"/>
    </svg>
    <div class="brand" style="top:74px">
      <span class="brand__name"><span class="brand__mark"></span>Brightvane Panel Wash</span>
    </div>

    <div class="why">
      <div class="why__line1">The biggest Thing to</div>
      <div class="why__line2">Highlight is WHY?</div>
    </div>
    <div class="rule-green" style="top:583px"></div>
    <div class="rule-blue" style="top:598px"></div>

    <div class="services">
      <div class="services__tab">Services</div>
      <div class="services__copy">
        <p><span class="hl">Brightvane Panel Wash</span> specialises only in cleaning solar panels, whether it's a full solar panel system or a smaller hot water system, Brightvane Panel Wash can handle the job for you.</p>
        <p>Our unique cleaning system will ensure your solar panels maximise their output to provide you with increased energy and deliver you huge savings!</p>
      </div>
      <div class="thumb thumb--panels" role="img" aria-label="Photo of a solar panel array"></div>
      <div class="thumb thumb--water" role="img" aria-label="Photo of a rooftop solar hot water system"></div>
      <div class="thumb__label" style="left:54px">Solar Panel System</div>
      <div class="thumb__label" style="left:273px">Solar Hot WaterSystem</div>
    </div>

    <div class="cta">For a free no obligation quote, enquiry or booking<br>please contact us today</div>
    <div class="cta-bar"></div>
    <div class="phone-pill">0412 555 308</div>
  </section>

  <section class="flyer flyer--back">
    <svg class="hero-art" width="540" height="290" viewBox="0 0 540 290" role="img" aria-label="Close-up photo of a cleaning brush on a solar panel">
      <defs>
        <linearGradient id="backPhoto" x1="0" y1="0" x2="1" y2="1">
          <stop offset="0" stop-color="#e8e8e8"/>
          <stop offset="0.45" stop-color="#a9abae"/>
          <stop offset="0.75" stop-color="#6f7378"/>
          <stop offset="1" stop-color="#9a9da1"/>
        </linearGradient>
        <linearGradient id="backFade" x1="0" y1="0" x2="0" y2="1">
          <stop offset="0" stop-color="#fff" stop-opacity="1"/>
          <stop offset="0.6" stop-color="#fff" stop-opacity="0.3"/>
          <stop offset="1" stop-color="#fff" stop-opacity="0"/>
        </linearGradient>
      </defs>
      <path d="M0,0 H540 V272 H260 C130,270 50,225 0,160 Z" fill="url(#backPhoto)"/>
      <rect x="0" y="0" width="540" height="120" fill="url(#backFade)"/>
      <path d="M0,160 C50,225 130,270 260,272 H540 V290 H0 Z" fill="#333333"/>
      <path d="M0,160 C50,225 130,270 260,274 H540" fill="none" stroke="#2bdc1e" stroke-width="7"/>
    </svg>
    <div class="brand" style="top:62px">
      <span class="brand__name"><span class="brand__mark"></span>Brightvane Panel Wash</span>
    </div>

    <div class="pricing-band"><div class="pricing-band__title">Pricing</div></div>
    <div class="rule-green" style="top:363px"></div>

    <div class="intro">
      <div class="intro__name">Brightvane Panel Wash</div>
      <div class="intro__text">has a very competitive<br>pricing model with</div>
      <div class="intro__offer">NO call out fee</div>
    </div>

    <div class="tier" style="top:618px">
      <div class="tier__head">Single Storey Residence</div>
      <div class="tier__price">$199*</div>
      <div class="tier__note">Includes up to 8 Solar Panels (2kW)<br>with Ground Access</div>
    </div>
    <div class="tier" style="top:762px">
      <div class="tier__head">Double Storey Residence</div>
      <div class="tier__price">$249*</div>
      <div class="tier__note">Includes up to 8 Solar Panels (2kW)<br>with Ground Access</div>
    </div>
    <div class="tier" style="top:902px">
      <div class="tier__head">Solar Hot Water System</div>
      <div class="tier__price">$159*</div>
      <div class="tier__note" style="left:165px">Contact us for a bundled deal</div>
    </div>

    <div class="footer-rule"></div>
    <div class="footer">
      <div class="footer__phone">0412 555 308</div>
      <div class="footer__web">brightvanepanelwash.com.au</div>
    </div>
  </section>

</div>
</body>
</html>
```